CD Album Cover Design For Emo Pop Punk Artist

Design an album cover for pop punk artist Milo Brandt's new album titled "Velvet Static" that captures his energetic performance style and signature aesthetic.

Brand Identity
- Artist: Milo Brandt
- Genre: Pop Punk / Alt Emo
- Trademark Colours: Pink and black
- Aesthetic: Gritty, energetic, raw

Design Requirements

Color Palette:
Primary: Vibrant pink (Milo's signature color)
Secondary: Deep black
Optional accents: White or silver for contrast

Image Treatment:
- Use one or more of the provided live performance photos
- Apply a grainy, slightly distressed texture for an authentic punk feel
- Consider a montage/collage approach if using multiple images
- High contrast treatment to enhance the pink/black dynamic

Typography:
- Album Title "Velvet Static" should be prominently featured
- Artist name "Milo Brandt" should be clearly visible
- Font style should reflect pop punk energy—but not be cheesy. slightly distressed, or bold sans-serif options
- Must have explicit content album sticker

Mood:
Convey intensity and energy that aligns with the "Velvet Static" title
Capture the raw excitement of a live performance
Create visual tension that draws the eye

Format Specifications
Dimensions: 4.75" × 4.75" (CD cover standard)
Resolution: 300 DPI minimum
Format: Print-ready PDF with 0.125" bleed
Additional formats: Square digital version (3000×3000px) for streaming platforms
Coverage: Both front and back covers required
Back Cover: Must include complete track listing with clean, legible typography while maintaining the design aesthetic

Optional Design Considerations
- Consider incorporating motion blur or duplicated elements to visually represent the "Velvet Static" concept
- Experiment with torn edges, noise overlays, or screen printing effects
- Explore the contrast between chaos (live performance energy) and focus (the album title concept)

Track list for back:
Cold window
KLR
7M
Sick of the noise
Lamplighter
Never Wave Twice
Past Your Porch
Wore Thin
Adrift
Sank Low
Pendulous [Track demo]

Front and back design is required! Logo is attached if needed too.

```html
<!DOCTYPE html>
<html lang="en">
<head>
<meta charset="utf-8">
<title>Velvet Static – Milo Brandt – CD Cover</title>
<link rel="stylesheet" href="https://fonts.googleapis.com/css2?family=Anton&family=Oswald:wght@400;500&family=Poppins:wght@400&display=swap">
<style>
  :root {
    --stage: #4a4a4a;
    --ink: #0d0b0d;
    --ink-soft: #1a1418;
    --pink: #c2548f;
    --pink-hot: #e04fb0;
    --pink-pale: #f2c6e2;
    --white: #f4f1f2;
    --muted: #d9d2d6;
  }
  * { box-sizing: border-box; margin: 0; padding: 0; }
  html, body {
    width: 1200px; height: 736px; overflow: hidden;
    background: var(--stage);
  }
  .spread {
    position: relative; width: 1200px; height: 736px;
    display: flex; gap: 40px; justify-content: center; align-items: center;
  }
  .cover {
    position: relative; width: 540px; height: 540px; overflow: hidden;
    background: var(--ink);
  }

  /* front */
  .cover-photo {
    position: absolute; inset: 0;
    background:
      radial-gradient(ellipse 40% 55% at 52% 40%, rgba(242,198,226,.85), rgba(224,79,176,.35) 55%, transparent 80%),
      radial-gradient(ellipse 25% 25% at 22% 32%, rgba(224,79,176,.7), transparent 75%),
      radial-gradient(ellipse 20% 30% at 90% 40%, rgba(224,79,176,.55), transparent 75%),
      linear-gradient(180deg, #2a0f22 0%, #1a0a16 60%, var(--ink) 100%);
  }
  .cover-shade {
    position: absolute; inset: 0;
    background: linear-gradient(180deg, transparent 55%, rgba(13,11,13,.92) 82%, var(--ink) 100%);
  }
  .label-mark {
    position: absolute; left: 38px; top: 30px;
    font-family: "Oswald", sans-serif; font-size: 9px; letter-spacing: .08em;
    color: var(--white); text-transform: uppercase;
  }
  .title {
    position: absolute; left: 0; right: 0; top: 370px;
    text-align: center;
    font-family: "Anton", sans-serif; font-size: 78px; line-height: 1;
    letter-spacing: -.01em; text-transform: uppercase;
    transform: skewX(-8deg) rotate(-3deg);
    text-shadow: 3px 3px 0 #000, -2px 2px 0 #000;
  }
  .title .title-a { color: var(--pink); }
  .title .title-b { color: var(--white); }
  .artist {
    position: absolute; right: 90px; top: 452px;
    font-family: "Anton", sans-serif; font-size: 28px; line-height: 1;
    color: var(--pink); text-transform: uppercase; letter-spacing: .02em;
    transform: rotate(-3deg);
    text-shadow: 2px 2px 0 #000;
  }

  /* back */
  .cover-back {
    background:
      radial-gradient(ellipse 70% 60% at 50% 45%, var(--ink-soft), var(--ink) 80%);
  }
  .tracklist {
    position: absolute; left: 44px; top: 44px; list-style: none;
    font-family: "Oswald", sans-serif; font-size: 13px; font-weight: 400;
    color: var(--white); text-transform: uppercase;
  }
  .tracklist li { height: 31.4px; display: flex; align-items: center; gap: 8px; }
  .tracklist .arrow { font-size: 9px; }
  .tracklist .time { margin-left: 12px; }
  .back-title {
    position: absolute; right: 36px; top: 44px; width: 200px; text-align: center;
    font-family: "Anton", sans-serif; font-size: 34px; line-height: 1;
    text-transform: uppercase; transform: skewX(-8deg) rotate(-3deg);
    text-shadow: 2px 2px 0 #000;
  }
  .back-title .title-a { color: var(--pink); }
  .back-title .title-b { color: var(--white); }
  .back-artist {
    position: absolute; right: 48px; top: 80px;
    font-family: "Anton", sans-serif; font-size: 13px; color: var(--pink);
    text-transform: uppercase; transform: rotate(-3deg);
  }
  .back-emblem {
    position: absolute; left: 250px; top: 170px; width: 230px; height: 230px;
    display: flex; align-items: center; justify-content: center;
  }
  .back-emblem span {
    position: relative;
    font-family: "Oswald", sans-serif; font-weight: 500; font-size: 34px;
    color: rgba(194,84,143,.35); text-transform: uppercase; letter-spacing: .04em;
  }
  .credits {
    position: absolute; left: 44px; top: 396px; width: 360px;
    font-family: "Poppins", sans-serif; font-size: 8.5px; line-height: 1.35;
    color: var(--muted);
  }
  .credits p + p { margin-top: 12px; }
  .sticker-slot {
    position: absolute; left: 355px; top: 460px; width: 124px; height: 44px;
    border: 1px solid var(--white);
  }
</style>
</head>
<body>
<main class="spread">
  <section class="cover cover-front">
    <div class="cover-photo" role="img" aria-label="Live performance photo in pink duotone: singer screaming into a microphone on stage with guitarist and drummer behind, grainy distressed texture"></div>
    <div class="cover-shade"></div>
    <div class="label-mark">Milo Brandt</div>
    <h1 class="title"><span class="title-a">Velvet</span> <span class="title-b">Static</span></h1>
    <p class="artist">Milo Brandt</p>
  </section>

  <section class="cover cover-back">
    <ol class="tracklist">
      <li><span class="arrow">&#9654;</span><span>1 Cold Window</span><span class="time">5:40</span></li>
      <li><span class="arrow">&#9654;</span><span>2 KLR</span><span class="time">3:30</span></li>
      <li><span class="arrow">&#9654;</span><span>3 7M</span><span class="time">4:06</span></li>
      <li><span class="arrow">&#9654;</span><span>4 Sick of the Noise</span><span class="time">3:26</span></li>
      <li><span class="arrow">&#9654;</span><span>5 Lamplighter</span><span class="time">4:56</span></li>
      <li><span class="arrow">&#9654;</span><span>6 Never Wave Twice</span><span class="time">4:16</span></li>
      <li><span class="arrow">&#9654;</span><span>7 Past Your Porch</span><span class="time">4:07</span></li>
      <li><span class="arrow">&#9654;</span><span>8 Wore Thin</span><span class="time">4:13</span></li>
      <li><span class="arrow">&#9654;</span><span>9 Adrift</span><span class="time">6:04</span></li>
      <li><span class="arrow">&#9654;</span><span>10 Sank Low</span><span class="time">5:30</span></li>
      <li><span class="arrow">&#9654;</span><span>11 Pendulous [Track Demo]</span><span class="time">5:30</span></li>
    </ol>
    <h2 class="back-title"><span class="title-a">Velvet</span> <span class="title-b">Static</span></h2>
    <p class="back-artist">Milo Brandt</p>
    <div class="back-emblem"><span>Milo Brandt</span></div>
    <div class="credits">
      <p>Produced, Recorded, and Mixed in Harlow Creek, OR by Reed Calloway</p>
      <p>&copy;Copyright 2025 Milo Brandt All Rights Reserved. Explore more at www.milobrandtmusic.net</p>
    </div>
    <div class="sticker-slot"></div>
  </section>
</main>
</body>
</html>
```